Custom Monogramming and Retail gifts

We need a Business Card for a monogramming business that offers many retail gift options. We are a home based business that uses social media (Chatterbook,clipboardly and our website) to sell our products. Our target market is college age, high school, baby gifts.
We want a preppy fun look. Monogramming is very popular in the South

Industry/Entity Type

College

Contact Information for Business Card

Threaded N' Charmed
Custom Monogramming and Gifts
5183 Larkmoor Lane
Brookhollow, GA 30999
Mona Prell, Owner
555-214-7390
threadedncharmed.example
threadedncharmed@mailbox.example

```html
<!DOCTYPE html>
<html lang="en">
<head>
<meta charset="utf-8">
<title>Threaded N' Charmed — Business Card</title>
<link rel="stylesheet" href="https://fonts.googleapis.com/css2?family=Arimo:wght@400&family=Lobster+Two:ital,wght@0,400;1,700&display=swap">
<style>
  :root {
    --page: #ffffff;
    --card: #ececea;
    --card-shade: #e2e2df;
    --pink: #f01fb4;
    --ink: #111111;
  }
  * { margin: 0; padding: 0; box-sizing: border-box; }
  html, body {
    width: 1200px;
    height: 885px;
    overflow: hidden;
    background: var(--page);
  }
  .canvas {
    position: relative;
    width: 1200px;
    height: 885px;
  }
  .card {
    position: absolute;
    left: 270px;
    top: 250px;
    width: 660px;
    height: 385px;
    background: linear-gradient(160deg, var(--card) 0%, var(--card-shade) 100%);
    overflow: hidden;
  }
  .stripe-band {
    position: absolute;
    left: 0;
    width: 100%;
    height: 16px;
    background: repeating-linear-gradient(
      to bottom,
      var(--pink) 0px,
      var(--pink) 2px,
      transparent 2px,
      transparent 4px
    );
  }
  .stripe-band--top { top: 12px; }
  .stripe-band--bottom { bottom: 14px; }

  .brand-name {
    position: absolute;
    left: 55px;
    top: 125px;
    width: 250px;
    text-align: center;
    font-family: "Lobster Two", cursive;
    font-weight: 400;
    font-size: 40px;
    line-height: 1.1;
    color: var(--pink);
  }
  .website {
    position: absolute;
    left: 70px;
    top: 298px;
    font-family: "Arimo", sans-serif;
    font-size: 16px;
    letter-spacing: 1px;
    color: var(--pink);
  }

  .header {
    position: absolute;
    left: 330px;
    top: 38px;
    width: 290px;
    text-align: center;
    font-family: "Lobster Two", cursive;
    font-style: italic;
    font-weight: 700;
    line-height: 1.15;
  }
  .header__name {
    font-size: 21px;
    letter-spacing: 1px;
    color: var(--pink);
  }
  .header__tagline {
    font-size: 17px;
    letter-spacing: 1px;
    color: var(--ink);
  }

  .contact {
    position: absolute;
    left: 355px;
    font-family: "Arimo", sans-serif;
    font-size: 12.5px;
    line-height: 1.3;
    color: var(--ink);
  }
  .contact--phone { top: 192px; }
  .contact--address { top: 218px; }
  .contact--email { top: 278px; }
</style>
</head>
<body>
<main class="canvas">
  <section class="card" aria-label="Business card">
    <div class="stripe-band stripe-band--top"></div>

    <p class="brand-name">Threaded N' Charmed</p>
    <p class="website">threadedncharmed.example</p>

    <header class="header">
      <p class="header__name">Threaded N' Charmed</p>
      <p class="header__tagline">Custom Monogramming<br>and Gifts</p>
    </header>

    <p class="contact contact--phone">555-214-7390</p>
    <p class="contact contact--address">5183 Larkmoor Lane<br>Brookhollow, GA 30999<br>Mona Prell, Owner</p>
    <p class="contact contact--email">threadedncharmed@mailbox.example</p>

    <div class="stripe-band stripe-band--bottom"></div>
  </section>
</main>
</body>
</html>
```